" Meu nome é Tarcísio Lobato e minha esposa, Celina Fagundes. Somos oftalmologistas e possuímos uma clínica oftalmológica com centro cirúrgico que atende a população da cidade de Pombal e cidades circunvizinhas. Apesar de já estarmos no mercado há mais de 10 anos, com clientela consolidada e de possuírmos uma logomarca, nunca conseguimos emplacar o nome da clínica, que sempre é conhecida como "Clínica da Dra. Celina". Ou seja, este é um "nome" forte que pode ser usado na nova marca. "

```html
<!DOCTYPE html>
<html lang="pt-BR">
<head>
<meta charset="UTF-8">
<title>Papel timbrado – VERANA</title>
<link href="https://fonts.googleapis.com/css2?family=Arimo:wght@400;700&family=Great+Vibes&display=swap" rel="stylesheet">
<style>
  :root {
    --bg: #e9e9ea;
    --paper: #ffffff;
    --brand-red: #c8202f;
    --ink: #1f1f1f;
    --muted: #555;
    --navy: #1f3a6b;
  }
  * { margin: 0; padding: 0; box-sizing: border-box; }
  html, body { width: 1200px; height: 1200px; overflow: hidden; }
  body {
    background: var(--bg);
    font-family: "Arimo", Arial, sans-serif;
    position: relative;
  }
  .letterhead {
    position: absolute;
    left: 250px; top: 105px;
    width: 700px; height: 990px;
    background: var(--paper);
    box-shadow: 0 4px 18px rgba(0,0,0,.18);
    overflow: hidden;
  }
  .top-stripe {
    position: absolute; left: 0; top: 0; width: 100%; height: 5px;
    background: linear-gradient(90deg, #e8392f, #f4a51c, #f2e21a, #6cc04a, #1fb3e5, #3a5fb8, #8e3f9a);
  }
  .brand {
    position: absolute; top: 78px; left: 0; width: 100%;
    display: flex; justify-content: center; align-items: center; gap: 16px;
  }
  .brand-dot {
    width: 58px; height: 58px; border-radius: 50%;
    background: var(--brand-red);
  }
  .brand-text { display: flex; flex-direction: column; }
  .brand-name {
    font-size: 54px; font-weight: 700; color: var(--brand-red);
    line-height: 1; letter-spacing: 1px;
  }
  .brand-tagline {
    font-size: 10.5px; font-weight: 700; color: var(--brand-red);
    text-transform: uppercase; margin-top: 5px;
  }
  .letter-body {
    position: absolute; left: 43px; top: 258px; width: 615px;
    font-size: 15.5px; line-height: 21.5px; color: var(--ink);
  }
  .letter-body p { margin-bottom: 21px; }
  .signature {
    position: absolute; right: 70px; top: 792px;
    font-family: "Great Vibes", cursive; font-size: 30px; color: var(--navy);
  }
  .contacts {
    position: absolute; left: 43px; top: 840px;
    display: grid; grid-template-columns: 210px 240px; column-gap: 10px; row-gap: 6px;
    font-size: 11px; color: var(--muted); line-height: 13px;
  }
  .contact { display: flex; gap: 6px; align-items: flex-start; }
  .contact svg { flex: none; margin-top: 1px; }
  .waves {
    position: absolute; left: 0; bottom: 0; width: 100%; height: 95px;
    background: linear-gradient(90deg, rgba(232,57,47,.55), rgba(244,165,28,.45) 20%, rgba(108,192,74,.35) 40%, rgba(31,179,229,.5) 60%, rgba(58,95,184,.55) 80%, rgba(142,63,154,.5));
    -webkit-mask: linear-gradient(to bottom, transparent, #000 70%);
            mask: linear-gradient(to bottom, transparent, #000 70%);
  }
</style>
</head>
<body>
  <main class="letterhead">
    <div class="top-stripe"></div>

    <header class="brand">
      <div class="brand-dot"></div>
      <div class="brand-text">
        <span class="brand-name">VERANA</span>
        <span class="brand-tagline">Clínica de Saúde e Bem-Estar do Sertão</span>
      </div>
    </header>

    <section class="letter-body">
      <p>Lorem ipsum dolor sit amet, ne vis ipsum detraxit forensibus. Vim ad dicta disputando, facete expetendis sea ne. At omnium vidisse referrentur cum. Id vel quas dicunt platonem, vim at veniam commodo adversarium, per an fabulas reformidans. Ad delenit appareat vel, denique minimum intellegam et has.</p>
      <p>Nec ex albucius moderatius. Essent salutandi pri id, no has porro commune. Iusto dolore definitionem mea et, eleifend salutatus at vel. Ignota aperiran duo an, nam no liber ceteros, sit legere saperet quaestio te. Sit ei oratio invenire platonem, nam ex congue primis conclusionemque, eos case albucius voluptatum cu.</p>
      <p>Sea ea summo senserit, ne pri accusam electram corrumpit. Hinc forensibus cu est, sed id invenire persequeris. Accumsan lucilius reformidans et sea. Duo laudem dolorem ne.</p>
      <p>Illud minimum duo ut. Docendi abhorreant duo no, duo ad appetere eleifend persequeris, blandit assentior disputationi no mea. Pro id movet cetero aeterno, in prima nusquam deseruisse pri, errem petentium et vis. Mollis aliquip admodum nec te, eu falli invenire iudicabit eu eam.</p>
      <p>Mei viderer adipisci corrumpit te, dissentias intellegebat per eu. An solum decore luptatum mei, in brute scripta disputationi vel. Semper gubergren quo no. In quo regione placerat, quod legere nam ad.</p>
    </section>

    <div class="signature">Nome Sobrenome</div>

    <footer class="contacts">
      <div class="contact">
        <svg width="10" height="12" viewBox="0 0 10 12"><path d="M2 0h2l1 3-1.5 1a6 6 0 0 0 3 3L7.5 5.5l2.5 1v2.5C10 10 9 11 8 11 3.5 10.5 0 6.5 0 2 0 1 1 0 2 0z" fill="#c8202f"/></svg>
        <span>(00) 0000.0000 / 0000.0000</span>
      </div>
      <div class="contact">
        <svg width="10" height="10" viewBox="0 0 10 10"><circle cx="5" cy="5" r="4.3" fill="none" stroke="#c8202f" stroke-width="1.2"/><path d="M1 5h8M5 1c-2 2.5-2 5.5 0 8M5 1c2 2.5 2 5.5 0 8" fill="none" stroke="#c8202f" stroke-width=".8"/></svg>
        <span>www.veranaexemplo.com.br</span>
      </div>
      <div class="contact">
        <svg width="11" height="9" viewBox="0 0 11 9"><rect x=".5" y=".5" width="10" height="8" fill="none" stroke="#c8202f"/><path d="M.5.5l5 4 5-4" fill="none" stroke="#c8202f"/></svg>
        <span>contato@veranaexemplo.com</span>
      </div>
      <div class="contact">
        <svg width="9" height="12" viewBox="0 0 9 12"><path d="M4.5 0A4.5 4.5 0 0 0 0 4.5C0 8 4.5 12 4.5 12S9 8 9 4.5A4.5 4.5 0 0 0 4.5 0z" fill="#c8202f"/><circle cx="4.5" cy="4.5" r="1.6" fill="#fff"/></svg>
        <span>End. completo, 00, Bairro<br>CEP 0000.0000 - Cidade-SP</span>
      </div>
    </footer>

    <div class="waves" role="img" aria-label="Faixas onduladas coloridas decorativas no rodapé"></div>
  </main>
</body>
</html>
```